Biz card for my counselling/social work practice

Biz card design for my counselling practice, focus on well-being, I am a social worker who also teaches meditation and workshops but my main focus for the card is my counselling practice. My website reveals a gentle flowing quality which I would life reflected in my card. This business card will be designed to share with other practitioners who are looking for support with their clients to take their healing to another level or well-being.

Target Market(s)

professionals seeking mental health counselling/men/women/ those seeking to improve their well-being through insight based counselling to optimize their lives and process trauma or limiting patterns

Industry/Entity Type

Counsellor

Contact Information for Business Card

Info on the card: perhaps text is aligned left?
Maribel Strand, MSW, RSW
Counsellor
614.295.3140
info@maribelstrand.example
www.maribelstrand.example

Please use a modern font doesn’t need to be the one chosen below. Thank you

Font styles to use
Serif

Colors
3176b5
33a6d7
33b8a4
6b449b
abd037
d2a4cc
e55fa2

Requirements
Must have
• My business card details on front
• Backside
• Accelerated Resolution Therapy
• Cognitive Behavioral Therapy
• Mindfulness Informed Therapy
Nice to have
• I would like the card to be basic, (white or creme without too much bold colour) and with perhaps a stripe or band of vertical colour in blue or green (or a merge of colour) perhaps embossed or in a negative space. (this is one idea, but do not want the card to be too feminine or interest only women as i see men too so this is only an idea, but not 100 percent on this.
• I do not have a logo. I would prefer to heart from my website not to be used in the design as i am considering modifying this and re-branding.
Should not have
• too bold colours or bright yellow/blacks. i Like tones that are greens, blues.

```html
<!DOCTYPE html>
<html lang="en">
<head>
<meta charset="utf-8">
<title>Maribel Strand – Business Card</title>
<link rel="stylesheet" href="https://fonts.googleapis.com/css2?family=Arimo:wght@400;700&display=swap">
<style>
  :root {
    --page-bg: #e9eaec;
    --card-white: #ffffff;
    --card-tint: #f4f7fd;
    --brand-blue: #1f5fd6;
    --ink: #1c1c1c;
    --ink-soft: #2d2d2d;
    --photo-sky: #dfe3e4;
    --photo-lake: #c9d0cf;
    --photo-green: #5d6b3c;
    --photo-brown: #7a6048;
    --photo-dark: #3a3029;
  }
  * { margin: 0; padding: 0; box-sizing: border-box; }
  html, body {
    width: 1200px; height: 901px; overflow: hidden;
    background: var(--page-bg);
    font-family: "Arimo", Arial, sans-serif;
  }
  .stage {
    position: relative; width: 1200px; height: 901px;
    display: flex; align-items: center; justify-content: center; gap: 40px;
  }
  .card {
    position: relative; width: 540px; height: 309px; overflow: hidden;
    box-shadow: 0 10px 28px rgba(0,0,0,.18);
  }

  /* Front: photo side */
  .card--front { background: var(--photo-sky); }
  .card__photo {
    position: absolute; inset: 0;
    background:
      radial-gradient(ellipse 30% 55% at 72% 55%, var(--photo-dark) 0%, rgba(58,48,41,.6) 60%, transparent 100%),
      linear-gradient(160deg, var(--photo-lake) 0%, var(--photo-sky) 30%, var(--photo-green) 55%, var(--photo-brown) 100%);
  }
  .front__welcome {
    position: absolute; left: 56px; top: 66px;
    font-size: 38px; font-weight: 400; color: var(--ink); letter-spacing: .3px;
  }
  .front__tagline {
    position: absolute; left: 66px; top: 110px;
    font-size: 14px; color: var(--ink-soft);
  }
  .front__services {
    position: absolute; left: 150px; top: 212px; list-style: none;
    font-size: 15px; line-height: 22px; color: var(--ink);
  }
  .front__services li:nth-child(2) { padding-left: 12px; }
  .front__services li:nth-child(3) { padding-left: 24px; }

  /* Back: contact side */
  .card--back { background: var(--card-tint); }
  .back__name {
    position: absolute; left: 58px; top: 76px;
    font-size: 27px; font-weight: 700; color: var(--brand-blue);
  }
  .back__role {
    position: absolute; left: 60px; top: 110px;
    font-size: 16px; color: var(--ink);
  }
  .back__contact {
    position: absolute; left: 190px; top: 214px;
    border-left: 1.5px solid var(--brand-blue);
    padding: 4px 0 4px 26px; list-style: none;
  }
  .back__contact li {
    display: flex; align-items: center; gap: 10px;
    font-size: 14px; line-height: 22px; color: var(--ink);
  }
  .back__contact svg { width: 15px; height: 15px; flex: none; }
</style>
</head>
<body>
<main class="stage">
  <section class="card card--front">
    <div class="card__photo" role="img" aria-label="Photograph of a smiling woman outdoors beside a lake with trees and grasses"></div>
    <h1 class="front__welcome">A Warm Welcome</h1>
    <p class="front__tagline">Therapy, Coaching, Yoga &amp; health</p>
    <ul class="front__services">
      <li>Accelerated Resolution Therapy</li>
      <li>Cognitive Behavioral Therapy</li>
      <li>Mindfulness Informed Therapy</li>
    </ul>
  </section>

  <section class="card card--back">
    <h2 class="back__name">Maribel Strand, MSW, RSW</h2>
    <p class="back__role">Counsellor</p>
    <ul class="back__contact">
      <li>
        <svg viewBox="0 0 16 16" aria-hidden="true"><path d="M3.5 1.5l2.5 2.8-1.4 1.6c.9 2 2.5 3.6 4.5 4.5l1.6-1.4 2.8 2.5-1.6 2c-5.2-.4-9.6-4.8-10-10z" fill="var(--brand-blue)"/></svg>
        614.295.3140
      </li>
      <li>
        <svg viewBox="0 0 16 16" aria-hidden="true"><rect x="1.5" y="3.5" width="13" height="9" fill="none" stroke="var(--brand-blue)" stroke-width="1.3"/><path d="M1.5 3.5L8 9l6.5-5.5" fill="none" stroke="var(--brand-blue)" stroke-width="1.3"/></svg>
        info@maribelstrand.example
      </li>
      <li>
        <svg viewBox="0 0 16 16" aria-hidden="true"><g fill="none" stroke="var(--brand-blue)" stroke-width="1.2"><circle cx="8" cy="8" r="6.3"/><ellipse cx="8" cy="8" rx="2.8" ry="6.3"/><path d="M1.7 8h12.6M2.8 5h10.4M2.8 11h10.4"/></g></svg>
        www.maribelstrand.example
      </li>
    </ul>
  </section>
</main>
</body>
</html>
```